Book Cover For Velvet Canyon Echoes

Need a book cover design to incorporate the following elements, which are attached. Size should be 6.125 x 9.25 niches. Explanation of attachments: 1) I drew up a sketch for the concept. 2) the artistic style from the Bali book would be preferable but not necessary. 3) I posted some images on a word doc to help create a visual of elements to include and some colors...the top image of the surfer on the word doc is a perfect style to copy. Also included at the bottom of the word doc are several images with color possibilities that can be experimented with. 4) Ideally, the font would be the golden encrusted royal font attached.
- all specifics are indicated on the rough sketch and images that are attached.

```html
<!DOCTYPE html>
<html lang="en">
<head>
<meta charset="UTF-8">
<title>Velvet Canyon Echoes — Book Cover</title>
<link rel="stylesheet" href="https://fonts.googleapis.com/css2?family=Cinzel:wght@400;700;900&display=swap">
<style>
  :root {
    --page-bg: #efefef;
    --sky-violet: #6a4a86;
    --sky-plum: #8c3f8e;
    --sky-magenta: #d8336e;
    --sky-pink: #f0709a;
    --sky-lilac: #c48fc0;
    --sky-gold: #ffd27a;
    --sky-glow: #fff3d6;
    --sea-horizon: #3f8fb0;
    --sea-foam: #d9ece8;
    --sea-teal: #27b5ad;
    --sea-deep: #0e6780;
    --surf-white: #e4efec;
    --sand: #c99a5a;
    --sand-dark: #9e733f;
    --shore-teal: #2fb3c0;
    --gold-light: #fff4c8;
    --gold-mid: #d8b562;
    --gold-dark: #7a5a22;
    --subtitle-gold: #f6e2a8;
    --author-white: #ffffff;
  }

  html, body {
    margin: 0;
    padding: 0;
    width: 1200px;
    height: 857px;
    overflow: hidden;
    background: var(--page-bg);
  }

  .stage {
    position: relative;
    width: 1200px;
    height: 857px;
  }

  .book-cover {
    position: absolute;
    left: 330px;
    top: 21px;
    width: 540px;
    height: 815px;
    overflow: hidden;
    box-shadow: 0 6px 18px rgba(0, 0, 0, 0.2);
  }

  .scene-sky {
    position: absolute;
    left: 0; right: 0; top: 0;
    height: 49%;
    background:
      radial-gradient(ellipse 40% 16% at 58% 100%, var(--sky-glow) 0%, rgba(255, 243, 214, 0) 100%),
      radial-gradient(ellipse 40% 12% at 30% 62%, rgba(140, 63, 142, 0.55) 0%, rgba(140, 63, 142, 0) 100%),
      radial-gradient(ellipse 35% 14% at 85% 45%, rgba(255, 170, 90, 0.6) 0%, rgba(255, 170, 90, 0) 100%),
      linear-gradient(180deg,
        var(--sky-violet) 0%,
        var(--sky-plum) 18%,
        var(--sky-magenta) 36%,
        var(--sky-pink) 52%,
        var(--sky-lilac) 66%,
        var(--sky-gold) 86%,
        var(--sky-glow) 100%);
  }

  .scene-sea {
    position: absolute;
    left: 0; right: 0;
    top: 49%;
    height: 38%;
    background:
      radial-gradient(ellipse 70% 12% at 50% 14%, rgba(228, 239, 236, 0.85) 0%, rgba(228, 239, 236, 0) 100%),
      radial-gradient(ellipse 30% 40% at 12% 55%, rgba(228, 239, 236, 0.6) 0%, rgba(228, 239, 236, 0) 100%),
      radial-gradient(ellipse 60% 30% at 55% 45%, rgba(14, 103, 128, 0.7) 0%, rgba(14, 103, 128, 0) 100%),
      linear-gradient(180deg,
        var(--sea-horizon) 0%,
        var(--sea-foam) 10%,
        var(--sea-teal) 28%,
        var(--sea-deep) 52%,
        var(--sea-teal) 66%,
        var(--surf-white) 74%,
        #8fb6b8 86%,
        #b9c7c2 100%);
  }

  .scene-beach {
    position: absolute;
    left: 0; right: 0;
    top: 87%;
    bottom: 0;
    background:
      linear-gradient(180deg,
        var(--sand) 0%,
        var(--sand-dark) 44%,
        var(--shore-teal) 52%,
        #3bbcc6 100%);
  }

  .title-block {
    position: absolute;
    left: 0;
    right: 0;
    top: 86px;
    text-align: center;
  }

  .book-title {
    margin: 0;
    font-family: "Cinzel", serif;
    font-weight: 900;
    line-height: 1.02;
    background: linear-gradient(180deg, var(--gold-light) 0%, var(--gold-mid) 45%, var(--gold-dark) 58%, var(--gold-mid) 75%, var(--gold-light) 100%);
    -webkit-background-clip: text;
    background-clip: text;
    color: transparent;
    filter: drop-shadow(2px 3px 2px rgba(40, 20, 10, 0.6));
  }

  .book-title .line-one {
    display: block;
    font-size: 56px;
  }

  .book-title .line-two {
    display: block;
    font-size: 56px;
  }

  .title-rule {
    width: 340px;
    height: 2px;
    margin: 4px auto 8px;
    background: var(--gold-mid);
  }

  .subtitle {
    margin: 0;
    font-family: "Cinzel", serif;
    font-weight: 400;
    font-size: 21px;
    line-height: 1.35;
    color: var(--subtitle-gold);
    text-shadow: 1px 1px 2px rgba(60, 20, 40, 0.55);
  }

  .author-name {
    position: absolute;
    left: 0;
    right: 0;
    bottom: 46px;
    margin: 0;
    text-align: center;
    font-family: "Cinzel", serif;
    font-weight: 700;
    font-size: 19px;
    letter-spacing: 1px;
    color: var(--author-white);
    text-shadow: 1px 1px 2px rgba(0, 0, 0, 0.55);
  }
</style>
</head>
<body>
  <main class="stage">
    <section class="book-cover">
      <div class="scene-sky" role="img" aria-label="Sunset sky in purple, magenta and gold with scattered clouds and seagulls over a glowing horizon"></div>
      <div class="scene-sea" role="img" aria-label="A large curling turquoise wave with a surfer riding it and white surf rolling toward the shore"></div>
      <div class="scene-beach" role="img" aria-label="Golden sand with a blue beach umbrella and a lounger where a person sits facing the sea"></div>

      <header class="title-block">
        <h1 class="book-title">
          <span class="line-one">Velvet Canyon</span>
          <span class="line-two">Echoes</span>
        </h1>
        <div class="title-rule"></div>
        <p class="subtitle">Four years to build a life<br>beyond the canyon</p>
      </header>

      <p class="author-name">Daniel Harwick</p>
    </section>
  </main>
</body>
</html>
```